Cybersecurity firm needs marketing template for professional services

Looking for a flyer design we can use as a template to market ten professional cybersecurity services (Pen Testing, V-CISO, SOC 2, VELMORA, etc). Each flyer will explain WHAT the service is, WHO needs it, DIFFERENT TYPES and SCOPE. Clean look/ lots of white space/ elevated graphics, Attached is a basic example but we are looking for something to WOW us.

```html
<!DOCTYPE html>
<html lang="en">
<head>
<meta charset="utf-8">
<title>Penetration Testing Flyer</title>
<link rel="stylesheet" href="https://fonts.googleapis.com/css2?family=Montserrat:wght@400;500;700&family=Oswald:wght@400;500&display=swap">
<style>
:root{
  --brand:#0b7cbd;
  --brand-deep:#0e5f96;
  --brand-mid:#2f86c2;
  --brand-soft:#3f95c9;
  --ice:#cfe3f0;
  --paper:#f6f6f6;
  --ink:#555a60;
  --white:#ffffff;
  --stage:#e9ecef;
}
*{margin:0;padding:0;box-sizing:border-box}
html,body{width:1200px;height:977px;overflow:hidden;background:var(--stage)}
.flyer{
  position:absolute;left:242px;top:20px;width:1003px;height:1313px;
  transform:scale(0.7137);transform-origin:0 0;
  background:var(--paper);overflow:hidden;font-family:"Montserrat",sans-serif;color:var(--ink);
}
.lower-wash{position:absolute;left:0;top:860px;width:560px;height:453px;
  background:linear-gradient(180deg,#5aa6d4 0%,var(--brand-soft) 100%)}
.content-panel{position:absolute;left:0;top:0;width:1003px;height:1155px;background:var(--paper);
  border-bottom-left-radius:230px}
.title{position:absolute;left:43px;top:40px;font-weight:700;font-size:74px;line-height:70px;color:var(--brand);letter-spacing:.5px}
.brand{position:absolute;left:700px;top:62px;display:flex;flex-direction:column;align-items:flex-end}
.brand-name{font-weight:500;font-size:29px;color:#6f7479;display:flex;align-items:center;gap:10px}
.brand-dot{width:18px;height:18px;border-radius:50%;background:var(--brand)}
.brand-tag{font-size:12.5px;color:#7b8086;margin-top:4px}
.what-box{position:absolute;left:0;top:207px;width:508px;height:276px;background:var(--brand);color:var(--white);padding:18px 8px 0 43px}
.what-box h2{font-size:36px;font-weight:700;line-height:40px;margin-bottom:10px}
.body-copy{font-size:17.6px;line-height:21.6px;hyphens:auto;-webkit-hyphens:auto}
.section{position:absolute;left:43px}
.section h2{font-size:30px;font-weight:700;color:var(--brand);line-height:34px;margin-bottom:6px}
.who{top:505px;width:470px}
.techniques{top:726px;width:560px}
.photo{position:absolute;left:524px;top:165px;width:479px;height:663px;
  background:linear-gradient(160deg,#e8eef3 0%,#b9cfe0 40%,#7fa4c2 75%,#dfe6ec 100%);
  border-radius:190px 170px 0 230px}
.cycle{position:absolute;left:60px;top:855px;width:290px;height:290px}
.cycle text{font-family:"Oswald",sans-serif}
.tools{position:absolute;left:387px;top:870px;width:575px}
.tools h2{font-size:32px;font-weight:700;color:var(--brand);line-height:36px;margin-bottom:12px}
.tools p{text-align:justify;hyphens:none;-webkit-hyphens:none}
.cta{position:absolute;left:387px;top:1090px;width:575px;font-family:"Oswald",sans-serif;font-weight:500;font-size:32px;line-height:40px;color:var(--brand-mid);white-space:nowrap}
.footer{position:absolute;left:0;top:1155px;width:1003px;height:158px;background:var(--brand-soft);border-top-right-radius:110px;color:var(--white)}
.contact{position:absolute;left:58px;top:24px;font-family:"Oswald",sans-serif;font-size:19px;line-height:30px;font-weight:400}
.contact b{font-weight:500}
.call{position:absolute;left:445px;top:8px;width:525px;text-align:center}
.call-label{font-size:29px;font-weight:700;line-height:36px}
.call-number{margin-top:8px;height:74px;border-radius:40px;background:var(--white);color:#1d7fc0;font-size:68px;font-weight:700;line-height:74px;letter-spacing:1px}
</style>
</head>
<body>
<main class="flyer">
  <div class="lower-wash"></div>
  <div class="content-panel"></div>

  <h1 class="title">Penetration<br>Testing...</h1>

  <div class="brand">
    <div class="brand-name"><span class="brand-dot"></span>Corvane Group</div>
    <div class="brand-tag">Cybersecurity | Risk | Audit | Advisory</div>
  </div>

  <section class="what-box">
    <h2>What it is...</h2>
    <p class="body-copy">A mature penetration test is an in-depth security assessment where ethical hackers attempt to exploit system vulnerabilities to gain access to sensitive data or systems. It is an important security practice because it can help organizations identify vulnerabilities that attackers may exploit in order to gain access to confidential information, disrupt services, or even cause physical damage to the network or system.</p>
  </section>

  <div class="photo" role="img" aria-label="Photo of a glass office tower seen from below against a pale sky"></div>

  <section class="section who">
    <h2>Who needs it</h2>
    <p class="body-copy">Any organization that wants to assess the security of their networks or applications, as well as identify potential vulnerabilities, should consider a penetration test. Examples might include financial institutions, healthcare companies, government entities, or any other organization that stores or manages sensitive data.</p>
  </section>

  <section class="section techniques">
    <h2>Testing Techniques</h2>
    <p class="body-copy">A wide range of techniques are used to identify security weaknesses, such as vulnerability scanning, application security testing, manual testing, and web application testing.</p>
  </section>

  <svg class="cycle" viewBox="-145 -145 290 290" aria-label="Pen test cycle diagram">
    <g fill="none" stroke-width="50">
      <circle r="100" pathLength="360" stroke="#cfe3f0" stroke-dasharray="89 271" transform="rotate(-140)"/>
      <circle r="100" pathLength="360" stroke="#0e5f96" stroke-dasharray="49 311" transform="rotate(-50)"/>
      <circle r="100" pathLength="360" stroke="#2a78b2" stroke-dasharray="49 311" transform="rotate(0)"/>
      <circle r="100" pathLength="360" stroke="#3d8bc4" stroke-dasharray="59 301" transform="rotate(50)"/>
      <circle r="100" pathLength="360" stroke="#7fb6dd" stroke-dasharray="44 316" transform="rotate(110)"/>
      <circle r="100" pathLength="360" stroke="#a8cde8" stroke-dasharray="64 296" transform="rotate(155)"/>
    </g>
    <g stroke="#ffffff" stroke-width="1.5">
      <line x1="0" y1="0" x2="138" y2="0" transform="rotate(-140)"/>
      <line x1="0" y1="0" x2="138" y2="0" transform="rotate(-50)"/>
      <line x1="0" y1="0" x2="138" y2="0" transform="rotate(0)"/>
      <line x1="0" y1="0" x2="138" y2="0" transform="rotate(50)"/>
      <line x1="0" y1="0" x2="138" y2="0" transform="rotate(110)"/>
      <line x1="0" y1="0" x2="138" y2="0" transform="rotate(155)"/>
    </g>
    <g fill="#ffffff">
      <circle cx="-106" cy="-89" r="3"/><circle cx="89" cy="-106" r="3"/><circle cx="138" cy="0" r="3"/>
      <circle cx="89" cy="106" r="3"/><circle cx="-47" cy="130" r="3"/><circle cx="-125" cy="58" r="3"/>
    </g>
    <circle r="73" fill="#ffffff"/>
    <circle r="60" fill="none" stroke="#dde9f3" stroke-width="7"/>
    <circle r="60" fill="none" stroke="#2a86c2" stroke-width="7" pathLength="360" stroke-dasharray="250 110" transform="rotate(-90)"/>
    <text x="0" y="-6" text-anchor="middle" font-size="21" fill="#2a86c2">Pen Test</text>
    <text x="0" y="17" text-anchor="middle" font-size="21" fill="#2a86c2">cycle</text>
    <text x="10" y="-96" text-anchor="middle" font-size="14" fill="#ffffff">Research</text>
    <text transform="translate(92,-36) rotate(70)" text-anchor="middle" font-size="14" fill="#ffffff">Cleanup</text>
    <text transform="translate(86,34) rotate(-65)" text-anchor="middle" font-size="14" fill="#ffffff">Report</text>
    <text transform="translate(103,40) rotate(-65)" text-anchor="middle" font-size="14" fill="#ffffff">Writing</text>
    <text transform="translate(25,97) rotate(-15)" text-anchor="middle" font-size="14" fill="#ffffff">Enumeration</text>
    <text transform="translate(-70,72) rotate(50)" text-anchor="middle" font-size="14" fill="#ffffff">Scanning</text>
    <text transform="translate(-92,-10) rotate(-80)" text-anchor="middle" font-size="14" fill="#ffffff">Scope</text>
  </svg>

  <section class="tools">
    <h2>Testing Tools</h2>
    <p class="body-copy">1. PortLens 2. ProxyForge 3. ExploitBay 4. PacketTide 5. Hashbreaker Jack 6. WebProbe 7. ServScan 8. QueryMapper 9. VulnSight 10. LoginStorm 11. AirSplit 12. SignalWatch 13. AuthCrack 14. GridMap 15. HostGuard 16. DirAudit 17. NetWander 18. NameScan 19. LinkTap 20. AppProbe 21. PingCraft 22. OpenAssess 23. SocialKit 24. PortLens Script Engine 25. CoreStrike 26. GraphIntel 27. MetaSift 28. WebCrawlr 29. SiteFish 30. OpenZapper</p>
  </section>

  <p class="cta">Considering a Pen Test? Contact Our Expert</p>

  <footer class="footer">
    <div class="contact">
      <p><b>Phone:</b> + 800-555-0142</p>
      <p><b>Mailbox:</b> pentest@corvanepro.com</p>
      <p><b>Address:</b> 410 W. Harbor Lane<br>Suite 120 Lakeview, OH 44012</p>
    </div>
    <div class="call">
      <p class="call-label">Call Now</p>
      <p class="call-number">800-555-0142</p>
    </div>
  </footer>
</main>
</body>
</html>
```